Window Cleaning Leaflet

Hi everyone,

I need a leaflet (couldn't find 'leaflet' as an option when begining this project - so one sided only) to send out to coastal properties in South side Melbourne. The Flyer is aimed at high net individuals, mummies, business people etc who own these properties who don't have time to clean the windows themselves (often multiple levels) and want their home looking fabulous in time for Christmas and NY's celebrations.

I would really love a new and original design for a window washing leaflet. something outside of the norm that 'pops' and makes people feel happy when they look at it.

I guess a point of differentiation is that I'm a female working in a mans industry so appeal to mothers looking for someone who is 'reliable, trustworthy and understanding of peoples needs'.

I have made an outline of what I would like included in the leaflet, so if you could please take a look, feel free to change things around, wording and layout etc. If you can make it sound more professional please do so.

I would like the colours to be 'happy' colours, maybe with a silly season theme?

Overall aesthetically pleasing is a must, I find most window cleaning leaflets fairly mundane and boring, please feel free to think outside the box. The more original the better.

Target Market(s)

People who own large Melbourne homes in affluent suburbs, mainly suburbs with a lot of large coastal properties. Generally owned by high net worth individuals who just don't have tme to clean the windows themselves due to their profession or hectic lifestyles but can afford to pay someone else to do it.

Industry/Entity Type

Window Cleaning

Requirements
Must have
• 1) The name of the business - Tilda’s Glass Gleaming Services
• 2) The coupon special and all details attached:
• Small Homes (up to 12 windows) $120
• Medium Homes (up to 16 windows) $180
• Large Homes (up to 20 windows, 2 storeys) $240
• 20% discount
• *Discount applicable to first time customers only.
• *All services include fly screen, sill and tracks cleaned as well as cobweb removal.
• *Houses with more than 20 windows (or two levels) will have an immediate quote provided upon inspection of the property with 20% discount applied.
• *Tilda’s Glass Gleaming Services are fully insured.
• 3) My contact number - 0418 263 591

```html
<!DOCTYPE html>
<html lang="en">
<head>
<meta charset="utf-8">
<title>Tilda’s Glass Gleaming Services – Christmas Leaflet</title>
<link href="https://fonts.googleapis.com/css2?family=Arimo:ital,wght@0,400;0,700;1,700&family=Play:wght@700&family=Roboto+Condensed:wght@700;800&display=swap" rel="stylesheet">
<style>
  :root {
    --backdrop: #5f5f5f;
    --paper: #ffffff;
    --cyan: #19b1d9;
    --blue: #0b7cc5;
    --pink: #e9559c;
    --ink: #2b2b2b;
    --rule: #9a9a9a;
    --card-edge: #cfcfcf;
    --room-red: #a3182a;
    --room-cream: #f3ece4;
    --room-pink: #efc8cc;
  }
  * { box-sizing: border-box; margin: 0; padding: 0; }
  html, body { width: 864px; height: 1200px; overflow: hidden; }
  body { background: var(--backdrop); position: relative; font-family: 'Arimo', Arial, sans-serif; }

  .leaflet {
    position: absolute; left: 77px; top: 96px; width: 710px; height: 1008px;
    background: var(--paper); overflow: hidden;
  }

  .hero {
    position: absolute; left: 0; top: 0; width: 710px; height: 470px;
    background:
      linear-gradient(180deg, rgba(255,255,255,0) 62%, rgba(255,255,255,.85) 88%, #ffffff 100%),
      linear-gradient(90deg, var(--room-red) 0%, #b02a38 30%, #d9a7a4 44%, var(--room-cream) 54%, #f8f3ee 72%, var(--room-pink) 100%);
  }
  .hero-cut { position: absolute; left: 0; top: 0; }

  .discount-badge {
    position: absolute; left: 42px; top: 284px; width: 174px; height: 174px;
    border-radius: 50%; background: var(--cyan); border: 6px solid var(--paper);
    box-shadow: 0 2px 6px rgba(0,0,0,.25);
    color: var(--paper); font-family: 'Roboto Condensed', 'Arial Narrow', sans-serif; font-weight: 800;
    display: flex; flex-direction: column; align-items: center; justify-content: center;
    transform: rotate(-14deg);
  }
  .discount-badge .value { font-size: 62px; line-height: 56px; }
  .discount-badge .label { font-size: 28px; line-height: 30px; }

  .business-name {
    position: absolute; left: 45px; top: 478px;
    font-family: 'Play', 'Trebuchet MS', sans-serif; font-weight: 700;
    font-size: 52px; line-height: 62px; color: var(--blue); letter-spacing: 0;
  }

  .questions {
    position: absolute; left: 43px; top: 626px; width: 182px;
    font-style: italic; font-weight: 700; font-size: 18px; line-height: 23px; color: var(--cyan);
  }
  .questions p + p { margin-top: 23px; }

  .divider { position: absolute; left: 234px; top: 626px; width: 1px; height: 170px; background: var(--rule); }

  .pitch {
    position: absolute; left: 247px; top: 628px; width: 286px;
    font-size: 17.5px; line-height: 22px; color: var(--ink);
  }
  .pitch p + p { margin-top: 22px; }

  .price-card {
    position: absolute; left: 562px; width: 120px; height: 112px;
    border: 2px solid var(--card-edge); border-radius: 12px; background: var(--paper);
    box-shadow: 0 2px 3px rgba(0,0,0,.12); overflow: hidden; text-align: center;
    font-family: 'Roboto Condensed', 'Arial Narrow', sans-serif; font-weight: 700;
  }
  .price-card .head { height: 80px; color: var(--paper); padding-top: 9px; }
  .price-card .tier { font-size: 14px; line-height: 16px; }
  .price-card .price { font-size: 46px; line-height: 48px; font-weight: 800; }
  .price-card .note { color: var(--ink); font-size: 13px; line-height: 14px; padding-top: 6px; }
  .price-card.small { top: 440px; } .price-card.small .head { background: var(--cyan); }
  .price-card.medium { top: 563px; } .price-card.medium .head { background: var(--blue); }
  .price-card.large { top: 687px; } .price-card.large .head { background: var(--pink); }
  .price-card.large .note { padding-top: 2px; line-height: 13px; }

  .call-bar { position: absolute; left: 0; top: 817px; width: 710px; height: 64px; display: flex; }
  .call-bar .offer {
    width: 351px; background: var(--cyan); color: var(--paper);
    font-family: 'Roboto Condensed', 'Arial Narrow', sans-serif; font-weight: 700;
    font-size: 19px; line-height: 22px; padding: 10px 0 0 37px;
  }
  .call-bar .phone {
    flex: 1; background: var(--blue); color: var(--paper);
    font-family: 'Roboto Condensed', 'Arial Narrow', sans-serif; font-weight: 800;
    font-size: 37px; line-height: 64px; padding-left: 15px; white-space: nowrap;
  }

  .conditions { position: absolute; left: 36px; top: 893px; width: 560px; list-style: none; font-size: 14px; line-height: 16px; color: var(--ink); }
  .conditions li { position: relative; padding-left: 15px; margin-bottom: 6px; }
  .conditions li::before { content: "*"; position: absolute; left: 0; top: 1px; font-weight: 700; }
  .fine-print { position: absolute; right: 26px; top: 985px; font-size: 10px; color: #555; }
</style>
</head>
<body>
  <main class="leaflet">
    <div class="hero" role="img" aria-label="Photo of a festive living room with a decorated Christmas tree, fireplace and wreath, with a hand holding a window squeegee wiping the glass"></div>
    <svg class="hero-cut" width="710" height="470" viewBox="0 0 710 470" aria-hidden="true">
      <polygon points="0,235 0,470 320,470" fill="#ffffff" opacity="0.8"/>
      <polygon points="560,0 710,0 710,120" fill="#ffffff" opacity="0.4"/>
    </svg>

    <div class="discount-badge">
      <span class="value">20%</span>
      <span class="label">Discount</span>
    </div>

    <h1 class="business-name">Tilda’s Glass<br>Gleaming Services</h1>

    <div class="questions">
      <p>Do you need your windows cleaned?</p>
      <p>Are you simply too busy as a hard working parent to do it yourself?</p>
    </div>
    <div class="divider"></div>
    <div class="pitch">
      <p>Tilda understands and wants to help you - enjoy your home looking it’s best before Christmas and NY’s celebrations begin.</p>
      <p>We provide a reliable, professional service, ensuring that your home will sparkle.</p>
    </div>

    <div class="price-card small">
      <div class="head"><div class="tier">SMALL HOMES</div><div class="price">$120</div></div>
      <div class="note">up to 12 windows</div>
    </div>
    <div class="price-card medium">
      <div class="head"><div class="tier">MEDIUM HOMES</div><div class="price">$180</div></div>
      <div class="note">up to 16 windows</div>
    </div>
    <div class="price-card large">
      <div class="head"><div class="tier">LARGE HOMES</div><div class="price">$240</div></div>
      <div class="note">up to 20 windows<br>&amp; 2 storeys</div>
    </div>

    <div class="call-bar">
      <div class="offer">Call Tilda today and take advantage<br>of our special introductory offer.</div>
      <div class="phone">Tilda : 0418 263 591</div>
    </div>

    <ul class="conditions">
      <li>Discount applicable to first time customers only.</li>
      <li>All services include fly screen, sill and tracks cleaned as well as cobweb removal.</li>
      <li>Houses with more than 20 windows (or two levels) will have an immediate quote provided upon inspection of the property with 20% discount applied.</li>
      <li>Tilda’s Glass Gleaming Services are fully insured.</li>
    </ul>
    <div class="fine-print">Condations Apply</div>
  </main>
</body>
</html>
```